Banner for homepage

It is a new banner for the homepage, temporary site address is 203.0.113.57 ( is the biggest banner only ) . Would be 5 variations for image content as below (in Portuguese ) :

Image 1:
Leitor de codigo de barras
Todos os tipos de leitores de código de barras para as mais diversas aplicações.
( example of product images in : http://www.quorvelidx.com/en-US/Pages/Category.aspx?category=barcode-scanners&cat=QMT)

Image 2:
Impressora de etiquetas
Identifique o que for nessário com o melhor custo/beneficio e flexibilidade de materiais de impressão.
( example of product images in : tarnix.com in label printers desktop and industrial)

Image 3:
Impressora de cupom
Imprima recibos e cupons fiscais com agilidade e qualidade, temos a impressora certa para o seu PDV.
( example of product images in : http://www.plivorato.com.br/equipamento-categoria-impressoras+fiscais.html)

Image 4:
Coletor de dados
Computadores móveis com leitor de código de barras, que levam a automação para frente de trabalho.
( example of product images in : http://www.quorvelidx.com/en-US/Pages/Category.aspx?cat=QMT&category=hand-held-mobile-computer)

Image 5:
Etiquetas e Ribbons:
Etiquetas adesivas e não adesivas em vários de tipos de materiais, papéis e plásticos. O ribbon certo para impressão perfeita em cada material.
( example of product images in : http://www.lumetrask.com/cats/supplies/barcode-printer.htm?nav=hdr)

```html
<!DOCTYPE html>
<html lang="pt-BR">
<head>
<meta charset="utf-8">
<title>Banners da página inicial</title>
<link rel="stylesheet" href="https://fonts.googleapis.com/css2?family=Open+Sans:wght@400;600&display=swap">
<style>
  :root {
    --page: #ffffff;
    --grey-light: #e6e6e6;
    --grey-mid: #bdbdbd;
    --grey-dark: #9a9a9a;
    --red: #d1353b;
    --red-dark: #b8262c;
    --text: #ffffff;
    --dot: #333333;
  }
  * { box-sizing: border-box; margin: 0; padding: 0; }
  html, body { width: 1200px; height: 800px; overflow: hidden; background: var(--page); }
  body { position: relative; font-family: "Open Sans", Arial, sans-serif; }

  .banner {
    position: absolute;
    overflow: hidden;
    background: radial-gradient(ellipse at 62% 50%, var(--grey-light) 0%, var(--grey-mid) 55%, var(--grey-dark) 100%);
  }
  .banner--scanner   { left: 6px;   top: 17px;  width: 586px; height: 233px; }
  .banner--labels    { left: 606px; top: 17px;  width: 586px; height: 233px; }
  .banner--receipt   { left: 256px; top: 263px; width: 688px; height: 274px; }
  .banner--collector { left: 6px;   top: 547px; width: 586px; height: 233px; }
  .banner--ribbons   { left: 610px; top: 547px; width: 580px; height: 233px; }

  .banner__bands { position: absolute; inset: 0; width: 100%; height: 100%; }
  .band { fill: var(--red); }
  .band--right { fill: var(--red-dark); }

  .banner__copy {
    position: absolute;
    color: var(--text);
    text-align: center;
    font-size: 12.5px;
    line-height: 1.3;
    text-shadow: 0 1px 2px rgba(0,0,0,.85);
  }
  .banner__title { text-decoration: underline; font-weight: 400; font-size: inherit; }
  .banner--receipt .banner__copy { font-size: 14.5px; }

  .product {
    position: absolute;
    border-radius: 14px;
    box-shadow: 0 0 28px 10px rgba(255,255,255,.55);
  }
  .product--dark  { background: linear-gradient(160deg, #5a5a5a, #1e1e1e); }
  .product--light { background: linear-gradient(160deg, #e9e6df, #8a8a8a); }
  .product--blue  { background: linear-gradient(160deg, #3a3a3a 0%, #1d3fbf 45%, #0a1f8c 100%); }

  .dots { position: absolute; right: 20px; bottom: 9px; display: flex; gap: 7px; }
  .dot { width: 9px; height: 9px; border: 1.5px solid var(--dot); border-radius: 50%; }
  .dot--active { width: 11px; height: 11px; margin-top: -1px; border-width: 2px; background: radial-gradient(circle, var(--dot) 0 35%, transparent 40%); }
</style>
</head>
<body>

<section class="banner banner--scanner">
  <svg class="banner__bands" viewBox="0 0 586 233" preserveAspectRatio="none" aria-hidden="true">
    <polygon class="band" points="0,62 330,112 330,148 0,205"/>
    <polygon class="band band--right" points="586,88 586,160 420,140 420,118"/>
  </svg>
  <div class="banner__copy" style="left:0;width:300px;top:86px;">
    <h2 class="banner__title">Leitor de codigo de barras</h2>
    <p>Todos os tipos de leitores de código<br>de barras para as mais diversas aplicações.</p>
  </div>
  <div class="product product--dark" style="left:300px;top:36px;width:175px;height:165px;" role="img" aria-label="Foto de leitores de código de barras de mão com base"></div>
  <div class="dots"><span class="dot dot--active"></span><span class="dot"></span><span class="dot"></span><span class="dot"></span><span class="dot"></span></div>
</section>

<section class="banner banner--labels">
  <svg class="banner__bands" viewBox="0 0 586 233" preserveAspectRatio="none" aria-hidden="true">
    <polygon class="band" points="0,62 350,112 350,148 0,205"/>
    <polygon class="band band--right" points="586,88 586,160 460,140 460,118"/>
  </svg>
  <div class="banner__copy" style="left:0;width:340px;top:86px;">
    <h2 class="banner__title">Impressora de etiquetas</h2>
    <p>Identifique o que for nessário com o melhor<br>custo/beneficio e flexibilidade de materiais de impressão.</p>
  </div>
  <div class="product product--light" style="left:340px;top:68px;width:175px;height:120px;" role="img" aria-label="Foto de impressoras de etiquetas de mesa e industrial"></div>
  <div class="dots"><span class="dot"></span><span class="dot dot--active"></span><span class="dot"></span><span class="dot"></span><span class="dot"></span></div>
</section>

<section class="banner banner--receipt">
  <svg class="banner__bands" viewBox="0 0 688 274" preserveAspectRatio="none" aria-hidden="true">
    <polygon class="band" points="0,55 390,125 390,170 0,225"/>
    <polygon class="band band--right" points="688,98 688,180 560,160 560,125"/>
  </svg>
  <div class="banner__copy" style="left:0;width:370px;top:105px;">
    <h2 class="banner__title">Impressora de cupom</h2>
    <p>Imprima recibos e cupons fiscais com agilidade e<br>qualidade, temos a impressora certa para o seu PDV.</p>
  </div>
  <div class="product product--dark" style="left:375px;top:62px;width:250px;height:168px;" role="img" aria-label="Foto de duas impressoras térmicas de cupom fiscal"></div>
  <div class="dots"><span class="dot"></span><span class="dot"></span><span class="dot dot--active"></span><span class="dot"></span><span class="dot"></span></div>
</section>

<section class="banner banner--collector">
  <svg class="banner__bands" viewBox="0 0 586 233" preserveAspectRatio="none" aria-hidden="true">
    <polygon class="band" points="0,48 370,112 370,148 0,190"/>
    <polygon class="band band--right" points="586,88 586,160 440,140 440,118"/>
  </svg>
  <div class="banner__copy" style="left:0;width:340px;top:86px;">
    <h2 class="banner__title">Coletor de dados</h2>
    <p>Computadores móveis com leitor de código de<br>barras, que levam a automação para frente de trabalho.</p>
  </div>
  <div class="product product--dark" style="left:368px;top:30px;width:98px;height:168px;" role="img" aria-label="Foto de dois coletores de dados portáteis com teclado"></div>
  <div class="dots"><span class="dot"></span><span class="dot"></span><span class="dot"></span><span class="dot dot--active"></span><span class="dot"></span></div>
</section>

<section class="banner banner--ribbons">
  <svg class="banner__bands" viewBox="0 0 580 233" preserveAspectRatio="none" aria-hidden="true">
    <polygon class="band" points="0,48 340,112 340,148 0,190"/>
    <polygon class="band band--right" points="580,88 580,160 470,140 470,118"/>
  </svg>
  <div class="banner__copy" style="left:0;width:290px;top:80px;">
    <h2 class="banner__title">Etiquetas e Ribbons:</h2>
    <p>Etiquetas adesivas e não adesivas em vários de<br>tipos de materiais, papéis e plásticos. O ribbon<br>certo para impressão perfeita em cada material.</p>
  </div>
  <div class="product product--blue" style="left:330px;top:38px;width:165px;height:170px;" role="img" aria-label="Foto de rolos de ribbon pretos e azuis"></div>
  <div class="dots"><span class="dot"></span><span class="dot"></span><span class="dot"></span><span class="dot"></span><span class="dot dot--active"></span></div>
</section>

</body>
</html>
```